NPG Job bank

Western Guild of Bracework Practitioners Needs a design for our orthodontist job bank.

We are in the process of redesigning our current job board. We would like to improve our current design, focusing on the landing page and possibly the search page. I have attached images of what we currently have in place right now.

The Landing page: Currently, I find the landing page too wordy, members get confused when using it, we need something that is easier for providers are seekers to use. Set up more user friendly. Maybe have a button for become provider and become seeker and then a modal pops up with process.. The final design for this page needs to be user friendly, organized and clean. If someone were coming to this page for the first time they would know how to become a provider.

The search page: I was thinking it would be best to have the search options on the left hand side opposed to how it is just in the middle now. all of the information currently shown on this page needs to be included. The search results need improvement on how they are displayed as well.

If you have any questions feel free to contact me.

Industry/Entity Type

Bank

Number of Pages Required

1 page

Colors
33a6d7
85cae6
0692cd

Requirements
Must have
• A Landing page that is well designed and that is made in the blue colors that are shown on the attached files of what our job bank currently looks like. I have also attached 3 photos that could be used for a masthead, but keep in mind these do not have to be used, you can use any photo you would like, these are just for your convenience.
Nice to have
• An improved search results page along with the Landing page

```html
<!DOCTYPE html>
<html lang="en">
<head>
<meta charset="utf-8">
<title>NPG Job Bank — Practice Opportunities &amp; Careers</title>
<link href="https://fonts.googleapis.com/css2?family=Titillium+Web:wght@400;600&family=Open+Sans:wght@400;600;700&family=Oswald:wght@500&family=Roboto:wght@400;500;700&display=swap" rel="stylesheet">
<style>
:root{
  --top-bar:#166cab;
  --header:#1f97d1;
  --header-deep:#1589c4;
  --brand-light:#85cae6;
  --accent:#0692cd;
  --sky:#33a6d7;
  --navy:#0b3e7b;
  --card-top:#0e6aa8;
  --card-bottom:#023a78;
  --title:#1a5fa0;
  --body-text:#444;
  --footer-bg:#f4f6f8;
  --footer-link:#1d6aa8;
  --footer-head:#333;
  --white:#fff;
}
*{box-sizing:border-box;margin:0;padding:0}
html,body{width:918px;height:1200px;overflow:hidden;background:var(--white)}
body{position:relative;font-family:"Open Sans",sans-serif}
a{text-decoration:none;color:inherit}
.abs{position:absolute}

.utility-bar{left:0;top:0;width:918px;height:32px;background:linear-gradient(var(--top-bar),#1461a0)}
.utility-links{left:77px;top:10px;display:flex;gap:14px;font:700 8px "Open Sans",sans-serif;color:var(--brand-light)}
.benefits{left:744px;top:4px;width:97px;height:24px;background:var(--accent);border-radius:2px;color:var(--white);font:700 8px "Open Sans",sans-serif;padding:6px 8px}
.benefits svg{position:absolute;right:7px;top:8px}

.site-header{left:0;top:32px;width:918px;height:128px;background:linear-gradient(var(--header),var(--header-deep))}
.brand{left:77px;top:48px;display:flex;align-items:center;gap:10px}
.brand-mark{width:60px;height:58px;background:var(--white)}
.brand-name{font:400 15px/16px "Titillium Web",sans-serif;color:var(--brand-light);width:160px}
.tagline{left:77px;top:115px;font:400 10px "Titillium Web",sans-serif;color:var(--brand-light)}
.account{left:545px;top:72px;display:flex;align-items:center;gap:13px;font:500 19px "Oswald",sans-serif;color:var(--white)}
.account .divider{width:1px;height:26px;background:var(--white)}
.search{left:679px;top:69px;width:162px;height:24px;background:var(--white);border-radius:2px;font:400 10px "Roboto",sans-serif;color:#333;padding:5px 0 0 24px}
.search svg{position:absolute;left:8px;top:6px}
.main-nav{left:84px;top:134px;display:flex;gap:16px;font:400 14px "Titillium Web",sans-serif;color:var(--white);letter-spacing:-.2px}

.hero{left:0;top:160px;width:918px;height:380px;background:linear-gradient(100deg,#c9d3dc 0%,#eef2f5 35%,#b9c9d6 60%,#e6ebef 100%)}
.hero-arrow{top:335px;width:24px;height:24px}
.hero-dots{left:432px;top:519px;display:flex;gap:3px}
.hero-dots span{width:10px;height:10px;border-radius:50%;border:1.3px solid #333}
.hero-dots .active{background:var(--accent);border-color:#0c4f8a}

.intro{left:0;top:550px;width:918px;text-align:center}
.intro h1{font:400 24px "Titillium Web",sans-serif;color:var(--title)}
.intro p{font:400 10.2px/18.3px "Open Sans",sans-serif;color:var(--body-text);width:760px;margin:5px auto 0}

.role-card{top:666px;width:289px;height:170px;background:linear-gradient(var(--card-top),var(--card-bottom));color:var(--white);padding:13px 14px}
.role-card h2{font:400 19px "Titillium Web",sans-serif;line-height:24px}
.role-card h3{font:400 14px "Titillium Web",sans-serif;margin-top:3px}
.role-card ul{list-style:none;margin-top:4px;font:400 11px/18.3px "Titillium Web",sans-serif}
.role-icon{top:705px;width:76px;height:76px}

.site-footer{left:0;top:874px;width:918px;height:257px;background:var(--footer-bg);border-top:2px solid var(--navy)}
.footer-col{top:30px;font:400 11px "Roboto",sans-serif;color:var(--footer-link)}
.footer-col h4{font:500 11px "Roboto",sans-serif;color:var(--footer-head);margin-bottom:9px}
.footer-col li{list-style:none;margin-bottom:11.6px}
.partner{background:#dfe6ec}

.legal-bar{left:0;top:1131px;width:918px;height:69px;background:var(--navy);color:var(--white);font:600 10px "Open Sans",sans-serif}
.legal-items{position:absolute;left:62px;top:21px;width:790px;height:26px;display:flex;align-items:center;justify-content:space-between;white-space:nowrap}
.legal-items i{height:26px;border-left:1px dotted var(--white)}
.legal-code{position:absolute;left:872px;top:27px}
</style>
</head>
<body>

<header>
  <div class="abs utility-bar"></div>
  <nav class="abs utility-links"><a>Home</a><a>Store</a><a>Contact</a><a>NPG Member Directory</a><a>About</a></nav>
  <div class="abs benefits">Benefits For
    <svg width="8" height="6" viewBox="0 0 8 6"><path d="M1 1l3 3 3-3" fill="none" stroke="#fff" stroke-width="1.5"/></svg>
  </div>

  <div class="abs site-header"></div>
  <div class="abs brand"><span class="brand-mark"></span><span class="brand-name">Western Guild of Bracework Practitioners</span></div>
  <div class="abs tagline">Every Smile. Every Step. Every Practice.</div>
  <div class="abs account"><a>Join</a><span class="divider"></span><a>Sign In</a></div>
  <div class="abs search">Search
    <svg width="10" height="10" viewBox="0 0 10 10"><circle cx="4" cy="4" r="3" fill="none" stroke="#1f97d1" stroke-width="1.6"/><path d="M6.2 6.2L9 9" stroke="#1f97d1" stroke-width="1.6"/></svg>
  </div>
  <nav class="abs main-nav"><a>Meetings &amp; Events</a><a>Education</a><a>Practice Management</a><a>News &amp; Publications</a><a>Library &amp; Research</a><a>Legal &amp; Advocacy</a><a>Communities</a></nav>
</header>

<main>
  <div class="abs hero" role="img" aria-label="Photo of orthodontic professionals talking together around a tablet"></div>
  <svg class="abs hero-arrow" style="left:35px" viewBox="0 0 24 24"><circle cx="12" cy="12" r="11.5" fill="#fff" stroke="#bbb"/><path d="M14 7l-5 5 5 5" fill="none" stroke="#333" stroke-width="2.2"/></svg>
  <svg class="abs hero-arrow" style="left:855px" viewBox="0 0 24 24"><circle cx="12" cy="12" r="11.5" fill="#fff" stroke="#bbb"/><path d="M10 7l5 5-5 5" fill="none" stroke="#333" stroke-width="2.2"/></svg>
  <div class="abs hero-dots"><span class="active"></span><span></span><span></span></div>

  <section class="abs intro">
    <h1>Practice Opportunities &amp; Careers</h1>
    <p>The NPG offers a wide variety of educational opportunities for orthodontists, residents and orthodontic staff. We also provide career resources for members entering or transitioning out of practice, as well as members in academia.<br>What can we help you find? Use the arrows below to navigate to the information that applies to you: orthodontists, residents and orthodontic staff.</p>
  </section>

  <section class="abs role-card" style="left:123px">
    <h2>Provider</h2>
    <h3>Post an opportunity or Search Resumes</h3>
    <ul><li>Request Access</li><li>Post Opportunity</li><li>Search the Resume Center</li><li>Access Your Opportunities</li><li>Frequently Asked Questions</li></ul>
  </section>
  <svg class="abs role-icon" style="left:370px" viewBox="0 0 76 76">
    <circle cx="38" cy="38" r="38" fill="#fff"/><circle cx="38" cy="38" r="33" fill="#1ba8dc"/>
    <circle cx="38" cy="31" r="10" fill="#0a1f33"/><path d="M18 58c2-12 10-16 20-16s18 4 20 16z" fill="#0a1f33"/>
  </svg>

  <section class="abs role-card" style="left:481px">
    <h2>Seeker</h2>
    <h3>Find an Opportunity Upload Resume</h3>
    <ul><li>Request Access</li><li>Post Opportunity</li><li>Search the Resume Center</li><li>Access Your Opportunities</li><li>Frequently Asked Questions</li></ul>
  </section>
  <svg class="abs role-icon" style="left:724px" viewBox="0 0 76 76">
    <circle cx="38" cy="38" r="38" fill="#fff"/><circle cx="38" cy="38" r="33" fill="#1ba8dc"/>
    <path d="M25 26h26v3H25z M29 18h18l2 8H27z" fill="#0a1f33"/><circle cx="38" cy="34" r="9" fill="#0a1f33"/>
    <path d="M20 58c2-12 9-15 18-15s16 3 18 15z" fill="#0a1f33"/>
  </svg>
</main>

<footer>
  <div class="abs site-footer">
    <div class="abs footer-col" style="left:80px"><h4>About NPG</h4><ul><li>What We Do</li><li>Mission &amp; History</li><li>Governance</li><li>Financial Information</li><li>Strategic Plan</li></ul></div>
    <div class="abs footer-col" style="left:222px;top:34px"><ul><li>Awards</li><li>Advertise with Us</li><li>Calendar</li><li>Contact Us</li></ul></div>
    <div class="abs footer-col" style="left:363px"><h4>Membership</h4><ul><li>Join</li><li>Orthodontists</li><li>Students/Residents</li><li>Orthodontic Staff</li><li>International</li><li>International Students</li></ul></div>
    <div class="abs footer-col" style="left:505px"><h4>Tools</h4><ul><li>My NPG</li><li>NPG Communities</li><li>Member Directory</li><li>Webmail</li><li>CE Manager</li></ul></div>
    <div class="abs footer-col" style="left:646px"><h4>NPG Sites</h4><ul><li>NPG Foundation</li><li>mybracedsmile.org</li><li>NPG Insurance Company</li></ul></div>
    <div class="abs partner" style="left:648px;top:148px;width:86px;height:38px"></div>
    <div class="abs partner" style="left:752px;top:148px;width:86px;height:38px"></div>
    <div class="abs partner" style="left:654px;top:196px;width:84px;height:40px"></div>
    <div class="abs partner" style="left:744px;top:196px;width:90px;height:40px"></div>
  </div>

  <div class="abs legal-bar">
    <div class="legal-items">
      <span>© 2013 Western Guild of Bracework Practitioners</span><i></i>
      <span>218 Harbor Crest Ave. Portland, OR 97205</span><i></i>
      <span>(800) 555-0142 or (503) 555-0178</span><i></i>
      <span>Terms of Use Privacy Policy</span>
    </div>
    <span class="legal-code">X18</span>
  </div>
</footer>

</body>
</html>
```